We need a website design for an HVAC (Heating & Air Conditioning) Contractor*

Our HVAC client would like to have a more professional looking site as their current one (https://brisvanecomfortworks.example/) is a template site. We will be building the site in-house from the concept.
Items we'd like to incorporate:
- A banner on the homepage that has a click to call plus a form on the right side of the banner
- There is a video on the current website homepage, please find a place to incorporate this.
- We will need to have at least 800 words of content on the homepage, please find space for that (can be a description of a few of the heating / air conditioning services they do). Feel free to use filler content (lorem ipsum) if need be to just show how the content would look

All submissions must have a homepage and a related subpage concept.

Number of Pages Required

1 page

```html
<!DOCTYPE html>
<html lang="en">
<head>
<meta charset="utf-8">
<title>Brisvane Comfort Works – Heating &amp; Air Conditioning</title>
<link href="https://fonts.googleapis.com/css2?family=Roboto:wght@400;500;700&family=Barlow+Condensed:ital,wght@1,800&display=swap" rel="stylesheet">
<style>
:root{
  --red:#d22a26;
  --red-dark:#b71f1c;
  --blue:#0e3d8e;
  --blue-dark:#0a2f70;
  --text:#555;
  --heading:#222;
  --light:#f2f2f2;
  --white:#fff;
}
*{box-sizing:border-box;margin:0;padding:0}
html,body{width:1200px;height:3566px;overflow:hidden}
body{font-family:"Roboto",sans-serif;color:var(--text);background:var(--white);position:relative}
.abs{position:absolute}
.display{font-family:"Barlow Condensed",sans-serif;font-style:italic;font-weight:800;letter-spacing:-1px}
.brand-name{font-family:"Roboto",sans-serif;font-weight:700;color:var(--red);font-size:30px;display:flex;align-items:center;gap:10px}
.brand-name .mark{width:18px;height:18px;background:var(--blue);border-radius:50%}

/* header */
.site-header{left:0;top:0;width:1200px;height:115px}
.contact-item{display:flex;align-items:center;gap:12px}
.contact-item .ic{width:50px;height:50px;border-radius:50%;display:flex;align-items:center;justify-content:center}
.contact-item small{display:block;font-size:14px;color:#666}
.contact-item strong{display:block;font-size:17px;color:#222}
.contact-item.phone strong{font-size:22px}

.main-nav{left:0;top:115px;width:1200px;height:52px;background:var(--red)}
.main-nav ul{list-style:none;display:flex;position:absolute;left:93px;top:0;height:52px}
.main-nav li{color:#fff;font-size:15px;font-weight:500;padding:0 11px;line-height:52px}
.main-nav li.active{background:var(--blue);padding:0 16px}

/* hero */
.hero{left:0;top:167px;width:1200px;height:564px;background:linear-gradient(135deg,#8a3a2a 0%,#6b4a3a 40%,#6c6e6a 60%,#4d6b33 100%)}
.hero-title{left:110px;top:140px;color:#fff;font-size:58px;line-height:56px}
.hero-text{left:110px;top:278px;width:470px;color:#fff;font-size:16px;font-weight:500;line-height:26px}
.btn-slant{display:inline-flex;align-items:center;justify-content:center;gap:8px;background:var(--red);color:#fff;font-weight:700;clip-path:polygon(8% 0,100% 0,92% 100%,0 100%)}
.hero .btn-slant{position:absolute;left:110px;top:353px;width:180px;height:48px;font-size:16px}

.quote-panel{left:775px;top:98px;width:344px;height:538px;background:var(--blue)}
.quote-panel:before{content:"";position:absolute;right:-25px;top:0;border-left:25px solid var(--blue-dark);border-top:17px solid transparent}
.quote-panel h2{color:#fff;font-size:22px;font-weight:700;text-align:center;margin-top:22px;line-height:30px}
.field{position:absolute;left:31px;width:278px;height:58px;background:#fff;padding:8px 14px}
.field .lbl{font-size:13px;color:var(--blue);display:flex;align-items:center;gap:8px}
.field .lbl i{width:12px;height:12px;border:1.5px solid #aab;border-radius:3px;display:inline-block}
.field .ph{font-size:12px;color:#666;margin-top:6px}
.quote-panel .submit{position:absolute;left:31px;top:467px;width:278px;height:42px;background:var(--red);color:#fff;font-weight:700;font-size:16px;display:flex;align-items:center;justify-content:center}

/* about */
.about-media{left:111px;top:821px;width:502px;height:344px;background:linear-gradient(135deg,#d9d2c6,#9a7b62 55%,#3f3a3a)}
.play{position:absolute;left:220px;top:141px;width:62px;height:62px;border-radius:50%;background:var(--red);display:flex;align-items:center;justify-content:center}
.section-title{font-size:54px;line-height:60px}
.about-title{left:667px;top:822px;color:var(--blue)}
.about-title span,.services-title span{color:var(--red)}
.about-text{left:667px;top:896px;width:425px;font-size:14.5px;line-height:26px}
.about-text p{margin-bottom:10px}
.about .btn-slant{position:absolute;left:667px;top:1110px;width:170px;height:47px;font-size:14px}

/* services */
.services{left:0;top:1252px;width:1200px;height:653px;background:var(--light)}
.services-title{left:0;top:38px;width:1200px;text-align:center;color:var(--blue)}
.services-intro{left:160px;top:102px;width:880px;text-align:center;font-size:14.5px;line-height:25px}
.card{position:absolute;top:194px;width:309px;height:351px}
.card .photo{position:absolute;left:0;top:0;width:309px;height:241px}
.card .box{position:absolute;left:16px;top:155px;width:277px;height:196px;background:#fff;box-shadow:0 4px 12px rgba(0,0,0,.08);text-align:center;padding-top:52px}
.card .box:before{content:"";position:absolute;left:0;top:-28px;width:277px;height:30px;background:#fff;clip-path:polygon(0 100%,100% 0,100% 100%);border-top:0}
.card .redline{position:absolute;left:16px;top:124px;width:277px;height:34px}
.card h3{font-size:19px;font-weight:500;color:#222;margin-bottom:12px}
.card p{font-size:14px;line-height:21px;padding:0 24px;color:#777}
.card .go{position:absolute;right:0;bottom:0;width:44px;height:41px;background:var(--red);display:flex;align-items:center;justify-content:center}

/* why */
.why{left:0;top:1905px;width:1200px;height:488px;overflow:hidden}
.why-photo{left:560px;top:0;width:640px;height:488px;background:linear-gradient(135deg,#cfd0c8,#8b8f92 45%,#c7a78c 70%,#6b6a5e)}
.why-title{left:111px;top:60px;color:#fff;font-size:54px}
.why-text{left:111px;top:135px;width:450px;color:#fff;font-size:14.5px;line-height:24px}
.feat{position:absolute;display:flex;align-items:center;gap:14px;color:#fff;font-size:15.5px;font-weight:500;line-height:22px}
.feat .ic{width:62px;height:62px;border-radius:50%;background:var(--red);flex:none;display:flex;align-items:center;justify-content:center}

/* testimonials */
.clients-title{left:0;top:2460px;width:1200px;text-align:center;color:var(--blue)}
.quote-card{position:absolute;top:2605px;width:310px;height:190px;border:1.5px solid #e2e2e2;border-top:3px solid var(--red);border-radius:16px;padding:70px 26px 0;text-align:center;font-size:14.5px;line-height:26px;color:#666}
.avatar{position:absolute;top:2560px;width:92px;height:92px;border-radius:50%;background:linear-gradient(#cfc9c2,#6a6259);border:4px solid #fff}
.person{position:absolute;top:2816px;width:310px;text-align:center;font-size:15px;color:#222;font-weight:500}
.person small{font-size:10px;font-weight:400}
.stars{display:block;color:#f3b51b;font-size:13px;letter-spacing:1px;margin-top:4px}

/* cta */
.cta{left:0;top:2958px;width:1200px;height:237px;background:var(--red)}
.cta-title{left:0;top:34px;width:1200px;text-align:center;color:#fff;font-size:32px;line-height:36px}
.van{position:absolute;top:100px;width:325px;height:168px;background:linear-gradient(#f4f4f4,#d9d9d9);border-radius:40px 60px 14px 14px}
.cta-actions{left:360px;top:146px;display:flex;align-items:center;gap:14px}
.cta-btn{height:44px;display:flex;align-items:center;gap:6px;padding:0 20px;font-weight:700;font-size:14px}
.cta-or{color:#fff;font-size:18px;font-weight:500}

/* footer */
.site-footer{left:0;top:3195px;width:1200px;height:371px}
.footer-col h4{font-size:17px;color:#222;font-weight:500;margin-bottom:20px}
.footer-col li{list-style:none;font-size:13.5px;color:#666;margin-bottom:9px}
.social{display:flex;gap:8px}
.social span{width:32px;height:32px;border-radius:50%;display:block}
.ci{display:flex;gap:12px;margin-bottom:16px;font-size:13.5px;color:#666;line-height:18px}
.ci b{display:block;color:#222;font-size:12px;font-weight:700}
.copyright{left:0;top:337px;width:1200px;text-align:center;font-size:14px;color:#666;border-top:1px solid #eee;padding-top:14px;left:111px;width:978px}
.to-top{left:1107px;top:290px;width:34px;height:34px;border-radius:50%;background:var(--red);display:flex;align-items:center;justify-content:center}
</style>
</head>
<body>

<header class="site-header abs">
  <div class="abs" style="left:115px;top:38px"><div class="brand-name"><span class="mark"></span>Brisvane Comfort Works</div></div>
  <div class="abs contact-item" style="left:550px;top:27px">
    <div class="ic" style="background:var(--blue)"><svg width="24" height="18" viewBox="0 0 24 18"><rect x="1" y="1" width="22" height="16" rx="2" fill="none" stroke="#fff" stroke-width="2"/><path d="M1 2l11 8 11-8" fill="none" stroke="#fff" stroke-width="2"/></svg></div>
    <div><small>Email as on</small><strong>hello@brisvanecomfort.example</strong></div>
  </div>
  <div class="abs contact-item phone" style="left:860px;top:27px">
    <div class="ic" style="background:var(--red)"><svg width="24" height="24" viewBox="0 0 24 24"><path d="M6 2l4 5-2 3c1 3 3 5 6 6l3-2 5 4-3 4C10 21 3 14 2 5z" fill="#fff"/></svg></div>
    <div><small>24/7 Customer Service</small><strong>(555) 014-2290</strong></div>
  </div>
</header>

<nav class="main-nav abs">
  <ul><li class="active">Home</li><li>About Us</li><li>Services</li><li>Specials</li><li>Heart Financing</li><li>Testimonials</li><li>Contact Us</li></ul>
</nav>

<section class="hero abs" role="img" aria-label="Outdoor air conditioning unit beside a brick house with garden">
  <h1 class="hero-title abs display">Keep Your Friends And Family<br>Comfortable</h1>
  <p class="hero-text abs">We Now Offer A Full Line Of Sanitation Services To Combat Covid-19! Ask Us About These Services Today!</p>
  <a class="btn-slant">OUR SERVICES</a>
</section>

<aside class="quote-panel abs">
  <h2>Get Free Quotes From<br>Our Specialists!</h2>
  <div class="field" style="top:112px"><div class="lbl"><i></i>Name</div><div class="ph">Enter Your Full Name</div></div>
  <div class="field" style="top:182px"><div class="lbl"><i></i>Email</div><div class="ph">Enter Your Email Address</div></div>
  <div class="field" style="top:253px"><div class="lbl"><i></i>Phone</div><div class="ph">Enter Your Phone Number</div></div>
  <div class="field" style="top:323px"><div class="lbl"><i></i>State</div><div class="ph">Select Your State</div></div>
  <div class="field" style="top:394px"><div class="lbl"><i></i>Services</div><div class="ph">Select Your Services</div></div>
  <div class="submit">GET QUOTE NOW</div>
</aside>

<section class="about">
  <div class="about-media abs" role="img" aria-label="Video still of a family relaxing on a sofa at home">
    <div class="play"><svg width="22" height="24" viewBox="0 0 22 24"><path d="M2 1l19 11L2 23z" fill="#fff"/></svg></div>
  </div>
  <h2 class="about-title abs display section-title">About <span>Us</span></h2>
  <div class="about-text abs">
    <p>Lorem ipsum dolor sit amet, consectetur adipiscing elit, sed do eiusmod tempor incididunt ut labore et dolore magna aliqua. Ut enim ad minim veniam, quis nostrud exercitation ullamco laboris nisi ut aliquip ex ea commodo consequat. Duis aute irure dolor in reprehenderit in voluptate velit esse cillum.</p>
    <p>Lorem ipsum dolor sit amet, consectetur adipiscing elit, sed do eiusmod tempor incididunt ut labore magna aliqua.</p>
  </div>
  <a class="btn-slant">LEARN MORE <svg width="13" height="13" viewBox="0 0 14 14"><circle cx="7" cy="7" r="7" fill="#fff"/><path d="M5 4l3 3-3 3" stroke="#d22a26" stroke-width="2" fill="none"/></svg></a>
</section>

<section class="services abs">
  <h2 class="services-title abs display section-title"><span>Our</span> Services</h2>
  <p class="services-intro abs">Brisvane Comfort Works, LLC provides a wide variety of residential and commercial HVAC services in the Brisvane, OK area. With over a decade of experience, you can trust our HVAC company to install, repair and maintain the HVAC systems</p>

  <article class="card" style="left:111px">
    <div class="photo" role="img" aria-label="Boiler room with heating pipes and valves" style="background:linear-gradient(135deg,#e8e2da,#a9845f 60%,#6e5a48)"></div>
    <svg class="redline" viewBox="0 0 277 34" preserveAspectRatio="none"><path d="M0 34L277 0v5L0 34z" fill="#d22a26"/></svg>
    <div class="box"><h3>Heating</h3><p>Lorem ipsum dolor sit amet, consectetur adipiscing elit, sed do eiusmod tempor</p><div class="go"><svg width="18" height="10" viewBox="0 0 18 10"><path d="M0 5h15M11 1l4 4-4 4" stroke="#fff" stroke-width="2" fill="none"/></svg></div></div>
  </article>
  <article class="card" style="left:445px">
    <div class="photo" role="img" aria-label="Technician checking an outdoor air conditioning unit" style="background:linear-gradient(135deg,#b8c4d0,#707a84 55%,#2d2f33)"></div>
    <svg class="redline" viewBox="0 0 277 34" preserveAspectRatio="none"><path d="M0 34L277 0v5L0 34z" fill="#d22a26"/></svg>
    <div class="box"><h3>Air Conditioning</h3><p>Lorem ipsum dolor sit amet, consectetur adipiscing elit, sed do eiusmod tempor</p><div class="go"><svg width="18" height="10" viewBox="0 0 18 10"><path d="M0 5h15M11 1l4 4-4 4" stroke="#fff" stroke-width="2" fill="none"/></svg></div></div>
  </article>
  <article class="card" style="left:779px">
    <div class="photo" role="img" aria-label="Two workers in hard hats repairing rooftop units" style="background:linear-gradient(135deg,#c9ccd0,#8e9499 50%,#c84a3e 80%,#e9e0c0)"></div>
    <svg class="redline" viewBox="0 0 277 34" preserveAspectRatio="none"><path d="M0 34L277 0v5L0 34z" fill="#d22a26"/></svg>
    <div class="box"><h3>Repair &amp; maintenance</h3><p>Lorem ipsum dolor sit amet, consectetur adipiscing elit, sed do eiusmod tempor</p><div class="go"><svg width="18" height="10" viewBox="0 0 18 10"><path d="M0 5h15M11 1l4 4-4 4" stroke="#fff" stroke-width="2" fill="none"/></svg></div></div>
  </article>
</section>

<section class="why abs">
  <div class="why-photo abs" role="img" aria-label="Technician servicing the wiring of an air conditioning unit"></div>
  <svg class="abs" style="left:0;top:0" width="700" height="488" viewBox="0 0 700 488">
    <path d="M0 0H548L690 488H0z" fill="#d22a26"/>
    <path d="M0 0H530L665 444H0z" fill="#0e3d8e"/>
    <path d="M48 444H690V488H70L48 488 72 505z" fill="#d22a26"/>
    <path d="M48 466L72 444V488z" fill="#d22a26"/>
  </svg>
  <h2 class="why-title abs display">Why Choose Us?</h2>
  <p class="why-text abs">Your search for a timely, professional HVAC company ends here. All Brisvane Comfort Works offers HVAC installation and repair services in and around Brisvane &amp; Harlow Creek, OK.</p>
  <div class="feat" style="left:111px;top:236px"><span class="ic"><svg width="30" height="28" viewBox="0 0 30 28" fill="none" stroke="#fff" stroke-width="2"><path d="M3 27V17h5v10M12 27V11h5v16M21 27V5h5v22"/></svg></span>We have over 10<br>years experience</div>
  <div class="feat" style="left:344px;top:236px"><span class="ic"><svg width="28" height="28" viewBox="0 0 28 28" fill="none" stroke="#fff" stroke-width="2"><rect x="4" y="4" width="20" height="20" rx="3"/><circle cx="14" cy="14" r="5"/></svg></span>We offer free HVAC<br>replacement estimates</div>
  <div class="feat" style="left:111px;top:327px"><span class="ic"><svg width="28" height="28" viewBox="0 0 28 28" fill="none" stroke="#fff" stroke-width="2"><rect x="4" y="10" width="20" height="14" rx="2"/><path d="M10 10V5h8v5"/></svg></span>We offer HVAC<br>maintenance plans</div>
  <div class="feat" style="left:344px;top:327px"><span class="ic"><svg width="28" height="28" viewBox="0 0 28 28" fill="none" stroke="#fff" stroke-width="2"><path d="M3 13L14 4l11 9M6 11v13h16V11"/><rect x="11" y="16" width="6" height="8"/></svg></span>We provide residential &amp;<br>commercial HVAC services</div>
</section>

<h2 class="clients-title abs display section-title">What Our Clients Say</h2>
<div class="quote-card" style="left:111px">Sed ut perspiciatis unde omnis iste natus error sit voluptatem accusantium doloremque laudantium, totam rem aperiam, eaque ipsa quae ab illo</div>
<div class="quote-card" style="left:445px">Sed ut perspiciatis unde omnis iste natus error sit voluptatem accusantium doloremque laudantium, totam rem aperiam, eaque ipsa quae ab illo</div>
<div class="quote-card" style="left:779px">Lorem ipsum dolor sit consectetur adipiscing elit, sed do eiusmod tempor incididunt ut labore et dolore magna aliqua. Ut enim ad minim veniam,</div>
<div class="avatar" role="img" aria-label="Customer portrait" style="left:220px"></div>
<div class="avatar" role="img" aria-label="Customer portrait" style="left:554px"></div>
<div class="avatar" role="img" aria-label="Customer portrait" style="left:888px"></div>
<div class="person" style="left:111px">Dana Whitfield, <small>Chairman WBI</small><span class="stars">★★★★★</span></div>
<div class="person" style="left:445px">Lena Okafor, <small>Project Manager</small><span class="stars">★★★★★</span></div>
<div class="person" style="left:779px">Marcus Hale, <small>Chairman WBI</small><span class="stars">★★★★★</span></div>

<section class="cta abs">
  <h2 class="cta-title abs display">If A Air Conditioning For Geothermal System Installation<br>Services, Give Us A Call</h2>
  <div class="van" role="img" aria-label="White company service van" style="left:-20px"></div>
  <div class="van" role="img" aria-label="White company service van" style="left:878px"></div>
  <div class="cta-actions abs">
    <div class="cta-btn" style="background:#fff;color:var(--red)">REQUEST APPOINTMENT <svg width="13" height="13" viewBox="0 0 14 14"><circle cx="7" cy="7" r="7" fill="#d22a26"/><path d="M5 4l3 3-3 3" stroke="#fff" stroke-width="2" fill="none"/></svg></div>
    <span class="cta-or">Or</span>
    <div class="cta-btn" style="background:var(--blue);color:#fff"><svg width="12" height="12" viewBox="0 0 24 24"><path d="M6 2l4 5-2 3c1 3 3 5 6 6l3-2 5 4-3 4C10 21 3 14 2 5z" fill="#fff"/></svg><span style="font-size:11px;font-weight:400">CALL US:</span> 1234-567890</div>
  </div>
</section>

<footer class="site-footer abs">
  <div class="abs" style="left:111px;top:55px"><div class="brand-name" style="font-size:24px"><span class="mark"></span>Brisvane Comfort Works</div></div>
  <div class="abs social" style="left:143px;top:115px"><span style="background:#3b5998"></span><span style="background:#1da1f2"></span><span style="background:#dd4b39"></span><span style="background:#b83592"></span></div>
  <div class="abs footer-col" style="left:409px;top:35px"><h4>Quick Links</h4><ul><li>Home</li><li>About</li><li>Services</li><li>Gallery</li></ul></div>
  <div class="abs footer-col" style="left:629px;top:35px"><h4>About Company</h4><ul><li>Terms of Use</li><li>Terms &amp; Condition</li><li>News</li><li>Contact Us</li><li>FAQ</li></ul></div>
  <div class="abs footer-col" style="left:870px;top:35px;width:230px"><h4>Contact Us</h4>
    <div class="ci"><svg width="12" height="12" viewBox="0 0 24 24"><path d="M6 2l4 5-2 3c1 3 3 5 6 6l3-2 5 4-3 4C10 21 3 14 2 5z" fill="#d22a26"/></svg><div><b>Phone</b>(555) 014-2290</div></div>
    <div class="ci"><svg width="13" height="10" viewBox="0 0 24 18"><rect width="24" height="18" rx="2" fill="#d22a26"/><path d="M1 2l11 8 11-8" fill="none" stroke="#fff" stroke-width="2"/></svg><div><b>Email</b>hello@brisvanecomfort.example</div></div>
    <div class="ci"><svg width="10" height="14" viewBox="0 0 10 14"><path d="M5 0a5 5 0 015 5c0 4-5 9-5 9S0 9 0 5a5 5 0 015-5z" fill="#d22a26"/><circle cx="5" cy="5" r="2" fill="#fff"/></svg><div><b>Location</b>Lorem ipsum dolor sit amet, con elit, sed</div></div>
  </div>
  <div class="abs to-top"><svg width="12" height="8" viewBox="0 0 12 8"><path d="M1 7l5-5 5 5" stroke="#fff" stroke-width="2" fill="none"/></svg></div>
  <p class="abs copyright">2021 Copyright - Brisvane Comfort Works, LLC | All Rights Reserved</p>
</footer>

</body>
</html>
```